UI design needed for a prototype based on wireframe

Hey there.
I need a UI design done on a a prototype application idea before I send it to a programmer. Once designed and programmed the app will move onto a testing faze where it will stay for some time and, I assume, go through several redesign fazes. I have a wireframe mockup and background description so I imagine the design work is pretty straight forward. The app is an activity app that let´s users post different activities that they want to to and post it before a community of users who might be willing to participate. Any features worth mentioning might include Mingleport only log-in, Vantoro routes navigation and star rating system of the user. Besides that I think it´s fairly basic. This app will initially be launched only in vantoro stall because of the test feature of the marketplace.

```html
<!DOCTYPE html>
<html lang="en">
<head>
<meta charset="utf-8">
<title>Search Settings</title>
<link href="https://fonts.googleapis.com/css2?family=Roboto:wght@400;500;700&display=swap" rel="stylesheet">
<style>
  :root {
    --status-bg: #1e2225;
    --bar-bg: #2a2f33;
    --screen-bg: #2e3338;
    --divider: #25292d;
    --cell-line: #3b4146;
    --accent: #25b4c6;
    --accent-light: #b4f1f7;
    --muted: #5b6268;
    --muted-text: #6d747a;
    --title: #e9f3f5;
    --white: #ffffff;
  }
  * { box-sizing: border-box; margin: 0; padding: 0; }
  html, body { width: 675px; height: 1200px; overflow: hidden; }
  body {
    position: relative;
    background: var(--screen-bg);
    font-family: "Roboto", Arial, sans-serif;
  }
  .status-bar {
    position: absolute; left: 0; top: 0; width: 675px; height: 45px;
    background: var(--status-bg);
  }
  .status-bar .time {
    position: absolute; right: 18px; top: 9px;
    color: var(--white); font-size: 24px;
  }
  .status-bar svg { position: absolute; top: 10px; }
  .app-bar {
    position: absolute; left: 0; top: 45px; width: 675px; height: 105px;
    background: var(--bar-bg);
  }
  .app-bar .menu-icon { position: absolute; left: 34px; top: 40px; }
  .app-bar h1 {
    position: absolute; left: 137px; top: 32px;
    color: var(--title); font-size: 35px; font-weight: 500;
  }
  .section-label {
    position: absolute; left: 38px;
    color: var(--accent); font-size: 28px; font-weight: 500;
  }
  .divider {
    position: absolute; left: 0; width: 675px; height: 3px;
    background: var(--divider);
  }
  .gender-picker {
    position: absolute; left: 38px; top: 236px; width: 599px; height: 126px;
    border: 2px solid var(--cell-line); display: flex;
  }
  .gender-option {
    flex: 1; position: relative;
    border-left: 2px solid var(--cell-line);
    color: var(--muted); font-size: 23px; font-weight: 500; text-align: center;
  }
  .gender-option:first-child { border-left: none; }
  .gender-option svg { position: absolute; left: 50%; top: 26px; margin-left: -20px; }
  .gender-option span { position: absolute; left: 0; right: 0; top: 80px; }
  .gender-option.is-selected { color: var(--accent); }
  .range-value {
    position: absolute; font-size: 22px;
  }
  .range-value.min { left: 38px; color: var(--muted-text); }
  .range-value.max { right: 38px; color: var(--accent); font-weight: 500; }
  .slider { position: absolute; }
  .language-toggle { position: absolute; left: 556px; top: 1072px; }
</style>
</head>
<body>
  <div class="status-bar">
    <svg style="right:156px" width="30" height="26" viewBox="0 0 30 26"><path d="M1 3 L15 23 L29 3 Q15 -5 1 3Z" fill="#fff"/></svg>
    <svg style="right:118px" width="26" height="26" viewBox="0 0 26 26"><path d="M2 24 L24 24 L24 2Z" fill="#5c6166"/><path d="M2 24 L14 24 L14 12Z" fill="#fff"/></svg>
    <svg style="right:96px" width="14" height="26" viewBox="0 0 14 26"><rect x="4" y="0" width="6" height="3" fill="#fff"/><rect x="1" y="3" width="12" height="23" rx="1" fill="#fff"/></svg>
    <span class="time">12:30</span>
  </div>

  <header class="app-bar">
    <svg class="menu-icon" width="36" height="26" viewBox="0 0 36 26"><rect y="0" width="36" height="4" fill="#fff"/><rect y="11" width="36" height="4" fill="#fff"/><rect y="22" width="36" height="4" fill="#fff"/></svg>
    <h1>Search Settings</h1>
  </header>

  <div class="section-label" style="top:177px">See activities from:</div>
  <div class="gender-picker">
    <div class="gender-option is-selected">
      <svg width="40" height="40" viewBox="0 0 40 40"><circle cx="20" cy="20" r="18" fill="var(--accent)"/><path d="M11 20 L17.5 26.5 L29 14" stroke="#2e3338" stroke-width="4" fill="none"/></svg>
      <span>Men</span>
    </div>
    <div class="gender-option">
      <svg width="40" height="40" viewBox="0 0 40 40"><circle cx="20" cy="20" r="18" fill="var(--muted)"/><path d="M11 20 L17.5 26.5 L29 14" stroke="#2e3338" stroke-width="4" fill="none"/></svg>
      <span>Women</span>
    </div>
    <div class="gender-option">
      <svg width="40" height="40" viewBox="0 0 40 40"><circle cx="20" cy="20" r="18" fill="var(--muted)"/><path d="M11 20 L17.5 26.5 L29 14" stroke="#2e3338" stroke-width="4" fill="none"/></svg>
      <span>Both</span>
    </div>
  </div>
  <div class="divider" style="top:393px"></div>

  <div class="section-label" style="top:424px">Activities With KM ( kilometre ) :</div>
  <span class="range-value min" style="top:510px">70</span>
  <span class="range-value max" style="top:510px">150</span>
  <svg class="slider" style="left:79px;top:504px" width="486" height="40" viewBox="0 0 486 40">
    <line x1="0" y1="20" x2="486" y2="20" stroke="var(--cell-line)" stroke-width="3"/>
    <line x1="0" y1="20" x2="194" y2="20" stroke="var(--accent)" stroke-width="3"/>
    <circle cx="209" cy="20" r="14" fill="var(--screen-bg)" stroke="var(--accent)" stroke-width="3"/>
  </svg>
  <div class="divider" style="top:579px"></div>

  <div class="section-label" style="top:626px">Activities Cost ( USD ) :</div>
  <span class="range-value min" style="top:730px">120</span>
  <span class="range-value max" style="top:730px">500+</span>
  <svg class="slider" style="left:85px;top:724px" width="480" height="40" viewBox="0 0 480 40">
    <line x1="0" y1="20" x2="480" y2="20" stroke="var(--cell-line)" stroke-width="3"/>
    <line x1="0" y1="20" x2="141" y2="20" stroke="var(--accent)" stroke-width="3"/>
    <circle cx="156" cy="20" r="14" fill="var(--screen-bg)" stroke="var(--accent)" stroke-width="3"/>
  </svg>
  <div class="divider" style="top:798px"></div>

  <div class="section-label" style="top:838px">See Activities For :</div>
  <span class="range-value min" style="top:928px;font-size:21px">11 Sept, FRI</span>
  <span class="range-value max" style="top:928px;font-size:21px">Next Month</span>
  <svg class="slider" style="left:38px;top:950px" width="599" height="40" viewBox="0 0 599 40">
    <line x1="0" y1="20" x2="599" y2="20" stroke="var(--cell-line)" stroke-width="3"/>
    <line x1="0" y1="20" x2="217" y2="20" stroke="var(--accent)" stroke-width="3"/>
    <circle cx="232" cy="20" r="14" fill="var(--screen-bg)" stroke="var(--accent)" stroke-width="3"/>
  </svg>
  <div class="divider" style="top:1023px"></div>

  <div class="section-label" style="top:1079px">User With Some Language</div>
  <svg class="language-toggle" width="88" height="48" viewBox="0 0 88 48">
    <line x1="4" y1="24" x2="50" y2="24" stroke="var(--accent-light)" stroke-width="4" stroke-linecap="round"/>
    <circle cx="63" cy="24" r="21" fill="var(--accent-light)"/>
  </svg>
  <div class="divider" style="top:1155px"></div>
</body>
</html>
```